Website redesign for a technology and engineering company

We'd like to redesign our website which can be found on quorvane.co.nz
!! Please find the designers brief as an uploaded file with all details in there!!
The main purpose for redesign is:
>change of services offered
>old website not very user friendly to maintain or update
Key requirements:
>visually appealing
>easy to navigate
>simple and easy to read
>responsive
>mobile device compatibility
>integrating best SEO practice
All the details are in the attached designer brief document.

```html
<!DOCTYPE html>
<html lang="en">
<head>
<meta charset="utf-8">
<title>Quorvane — Precision. Efficiency. Clarity.</title>
<link href="https://fonts.googleapis.com/css2?family=Poppins:wght@300;400;500;600;700&display=swap" rel="stylesheet">
<style>
:root{
  --blue:#1f5ee8;
  --blue-bright:#2563f0;
  --hero-deep:#0a4a8c;
  --hero-mid:#1a6fb8;
  --navy:#070c3a;
  --ink:#111827;
  --text:#3a3f4b;
  --muted:#8a909c;
  --pale:#eff4fc;
  --panel:#f4f4f6;
  --white:#ffffff;
}
*{box-sizing:border-box;margin:0;padding:0}
html,body{width:1200px;height:4926px;overflow:hidden}
body{position:relative;font-family:"Poppins",sans-serif;color:var(--text);background:var(--white)}
.abs{position:absolute}
a{color:inherit;text-decoration:none}

/* hero */
.hero{left:0;top:0;width:1200px;height:690px;background:var(--pale)}
.hero-bg{left:0;top:0;width:1200px;height:690px}
.brand{font-weight:500;color:var(--white);font-size:30px;letter-spacing:.5px;display:flex;align-items:center;gap:10px}
.brand .dot{width:14px;height:14px;border-radius:50%;background:var(--white)}
.nav{left:415px;top:30px;display:flex;gap:46px;font-size:13px;color:var(--white)}
.nav .active{font-weight:600}
.btn-touch{left:920px;top:22px;width:138px;height:40px;border-radius:6px;background:var(--white);color:var(--ink);font-size:13px;font-weight:500;display:flex;align-items:center;justify-content:center;gap:6px}
.headline{left:204px;top:148px;color:var(--white);font-size:70px;line-height:78px;font-weight:300;letter-spacing:1px}
.headline strong{font-weight:700;display:block}
.swash{left:226px;top:380px}
.btn-contact{left:204px;top:422px;width:140px;height:42px;border-radius:6px;background:var(--white);color:var(--ink);font-size:13px;display:flex;align-items:center;justify-content:center;gap:6px}
.hero-photo{left:660px;top:0;width:540px;height:555px;border-bottom-right-radius:260px 240px;background:linear-gradient(160deg,#4f8fd6 0%,#7aa8d8 35%,#8e9aa6 60%,#5c646c 100%)}
.scroll-btn{left:568px;top:521px;width:62px;height:62px;border-radius:50%;background:var(--white);display:flex;align-items:center;justify-content:center;box-shadow:0 4px 14px rgba(0,0,0,.08)}
.mouse{width:18px;height:28px;border:2px solid var(--blue);border-radius:9px;position:relative}
.mouse:after{content:"";position:absolute;left:6px;top:8px;width:2px;height:6px;background:var(--blue)}

.section-title{left:0;width:1200px;text-align:center;font-size:38px;color:var(--ink);font-weight:400}
.section-title b{font-weight:600}

/* services */
.band{left:0;width:1200px}
.band.pale{background:var(--pale)}
.leaf{width:442px;height:442px;border-radius:50%}
.leaf.tl{border-top-left-radius:0}
.leaf.tr{border-top-right-radius:0}
.service h3{font-size:30px;font-weight:600;color:var(--ink);margin-bottom:14px}
.service ul{list-style:none}
.service li{font-size:14.5px;line-height:34px;display:flex;align-items:center;gap:8px;color:var(--text)}
.tick{width:14px;height:14px;flex:none}

/* about */
.about-box{left:0;top:2454px;width:600px;height:422px;background:var(--blue-bright);border-top-right-radius:14px;border-bottom-right-radius:14px}
.about-box h2{position:absolute;left:141px;top:52px;color:var(--white);font-size:32px;font-weight:600}
.about-box p{position:absolute;left:141px;width:410px;color:var(--white);font-size:11.5px;line-height:23px}
.btn-dark{position:absolute;left:141px;top:320px;width:140px;height:42px;border-radius:21px;background:var(--navy);color:var(--white);font-size:13px;display:flex;align-items:center;justify-content:center}
.about-photo{left:600px;top:2475px;width:600px;height:422px;border-top-left-radius:14px;background:linear-gradient(170deg,#6f7f8c 0%,#9aa3a8 40%,#c9772e 70%,#5e5a52 100%)}

/* cases */
.card{width:441px;height:413px;background:var(--white);border-radius:40px;box-shadow:0 8px 24px rgba(20,40,90,.08);overflow:hidden;text-align:center}
.card .ph{height:233px;border-radius:40px 40px 40px 40px}
.card h4{margin:36px auto 0;width:330px;font-size:15px;line-height:22px;font-weight:600;color:var(--ink)}
.card p{margin:12px auto 0;width:370px;font-size:11.5px;line-height:23px;color:var(--text)}
.card .go{position:absolute;left:201px;top:372px;width:38px;height:38px;border-radius:50%;background:var(--blue-bright);display:flex;align-items:center;justify-content:center}
.arrow-btn{width:34px;height:34px;border-radius:50%;display:flex;align-items:center;justify-content:center}

/* contact */
.contact-photo{left:141px;top:3562px;width:367px;height:537px;border-radius:14px;background:linear-gradient(180deg,#4d8fd8 0%,#9dc3e6 30%,#7a8f5e 65%,#3e5a2c 100%)}
.form-panel{left:531px;top:3594px;width:528px;height:314px;background:var(--panel);border-radius:14px}
.form-panel h2{position:absolute;left:36px;top:32px;font-size:28px;font-weight:600;color:var(--ink)}
.field{position:absolute;height:34px;border-bottom:1px solid #d7d9de;font-size:12px;color:var(--muted);display:flex;align-items:center;gap:8px}
.btn-submit{position:absolute;left:36px;top:240px;width:140px;height:40px;border-radius:20px;background:var(--blue-bright);color:var(--white);font-size:13px;display:flex;align-items:center;justify-content:center}
.board-photo{left:531px;top:3929px;width:287px;height:136px;border-radius:8px;background:linear-gradient(135deg,#2b2420 0%,#8a5a30 45%,#3a3432 100%)}
.years{left:841px;top:3929px;width:218px;height:136px;border-radius:8px;background:var(--blue-bright);color:var(--white);text-align:center;padding-top:28px}
.years b{display:block;font-size:42px;line-height:44px;font-weight:600}
.years span{font-size:14px}

/* newsletter */
.news-title{left:0;top:4196px;width:1200px;text-align:center;font-size:36px;font-weight:600;color:var(--ink)}
.news-note{left:0;top:4262px;width:1200px;text-align:center;font-size:11.5px;color:var(--text)}
.news-form{left:340px;top:4298px;width:495px;height:42px;border-radius:21px;background:var(--white);box-shadow:0 4px 14px rgba(0,0,0,.08);display:flex;align-items:center;padding-left:22px;font-size:11.5px;color:var(--text)}
.news-form .sub{position:absolute;right:0;top:0;width:138px;height:42px;border-radius:21px;background:var(--blue-bright);color:var(--white);font-size:12.5px;font-weight:500;display:flex;align-items:center;justify-content:center}

/* footer */
.footer-wave{left:0;top:4440px}
.footer{left:0;top:4560px;width:1200px;height:366px;background:var(--navy);color:var(--white)}
.footer .about{position:absolute;left:141px;top:180px;width:270px;font-size:10.5px;line-height:17px;color:#d7daf0}
.footer h5{position:absolute;font-size:13.5px;font-weight:400}
.footer h5 b{font-weight:600}
.links{position:absolute;left:467px;top:110px;list-style:none;font-size:11.5px}
.links li{height:36px}
.cd{position:absolute;left:614px;font-size:11.5px;line-height:18px;display:flex;gap:10px}
.cd b{font-weight:600;display:block}
.big-mark{position:absolute;left:856px;top:50px;width:204px;height:204px;border-radius:50%;border:26px solid var(--white)}
.copy{position:absolute;left:141px;top:333px;font-size:11px;color:#d7daf0}
.legal{position:absolute;right:141px;top:333px;font-size:11px}
</style>
</head>
<body>

<!-- Hero -->
<div class="abs hero"></div>
<svg class="abs hero-bg" width="1200" height="690" viewBox="0 0 1200 690" aria-hidden="true">
  <defs>
    <linearGradient id="heroGrad" x1="0" y1="0" x2="1" y2="0">
      <stop offset="0" stop-color="#0b4f93"/>
      <stop offset="1" stop-color="#1f78c4"/>
    </linearGradient>
  </defs>
  <path d="M0 0H1200V555H190C90 555 20 610 0 690Z" fill="url(#heroGrad)"/>
</svg>
<div class="abs hero-photo" role="img" aria-label="Solar-powered GNSS monitoring station on a rocky alpine ridge under blue sky"></div>
<div class="abs brand" style="left:141px;top:24px"><span class="dot"></span>Quorvane</div>
<nav class="abs nav">
  <a class="active">Home</a><a>What We Do</a><a>About</a><a>Projects</a><a>Contact</a>
</nav>
<a class="abs btn-touch">Get In Touch
  <svg width="14" height="10" viewBox="0 0 14 10"><path d="M1 5h11M8 1l4 4-4 4" stroke="#111827" stroke-width="1.5" fill="none"/></svg></a>
<h1 class="abs headline">Precision.<br>Efficiency.<strong>Clarity.</strong></h1>
<svg class="abs swash" width="210" height="14" viewBox="0 0 210 14" aria-hidden="true"><path d="M2 10C70 2 140 2 208 6" stroke="#fff" stroke-width="3" fill="none" stroke-linecap="round"/></svg>
<a class="abs btn-contact">Contact Us
  <svg width="14" height="10" viewBox="0 0 14 10"><path d="M1 5h11M8 1l4 4-4 4" stroke="#111827" stroke-width="1.5" fill="none"/></svg></a>
<div class="abs scroll-btn"><div class="mouse"></div></div>

<h2 class="abs section-title" style="top:630px">Our <b>Services</b></h2>

<!-- Fieldwork -->
<div class="abs leaf tl" style="left:141px;top:701px;background:linear-gradient(160deg,#9aa7a0 0%,#4f6b43 50%,#6b6c66 100%)" role="img" aria-label="Field technician beside a solar-powered instrument frame on a roadside"></div>
<div class="abs service" style="left:682px;top:748px">
  <h3>Fieldwork Solutions</h3>
  <ul>
    <li><svg class="tick" viewBox="0 0 14 14"><circle cx="7" cy="7" r="7" fill="#1f5ee8"/><path d="M4 7l2 2 4-4" stroke="#fff" stroke-width="1.6" fill="none"/></svg>Project management &amp; logistics</li>
    <li><svg class="tick" viewBox="0 0 14 14"><circle cx="7" cy="7" r="7" fill="#1f5ee8"/><path d="M4 7l2 2 4-4" stroke="#fff" stroke-width="1.6" fill="none"/></svg>Efficient product rollouts</li>
    <li><svg class="tick" viewBox="0 0 14 14"><circle cx="7" cy="7" r="7" fill="#1f5ee8"/><path d="M4 7l2 2 4-4" stroke="#fff" stroke-width="1.6" fill="none"/></svg>Equipment Installation &amp; Maintenance</li>
    <li><svg class="tick" viewBox="0 0 14 14"><circle cx="7" cy="7" r="7" fill="#1f5ee8"/><path d="M4 7l2 2 4-4" stroke="#fff" stroke-width="1.6" fill="none"/></svg>Surveying Techniques</li>
    <li><svg class="tick" viewBox="0 0 14 14"><circle cx="7" cy="7" r="7" fill="#1f5ee8"/><path d="M4 7l2 2 4-4" stroke="#fff" stroke-width="1.6" fill="none"/></svg>Precision GNSS instrumentation</li>
    <li><svg class="tick" viewBox="0 0 14 14"><circle cx="7" cy="7" r="7" fill="#1f5ee8"/><path d="M4 7l2 2 4-4" stroke="#fff" stroke-width="1.6" fill="none"/></svg>Seismic Instrumentation</li>
    <li><svg class="tick" viewBox="0 0 14 14"><circle cx="7" cy="7" r="7" fill="#1f5ee8"/><path d="M4 7l2 2 4-4" stroke="#fff" stroke-width="1.6" fill="none"/></svg>IOT Sensors</li>
    <li><svg class="tick" viewBox="0 0 14 14"><circle cx="7" cy="7" r="7" fill="#1f5ee8"/><path d="M4 7l2 2 4-4" stroke="#fff" stroke-width="1.6" fill="none"/></svg>Reliable Communications Systems</li>
    <li><svg class="tick" viewBox="0 0 14 14"><circle cx="7" cy="7" r="7" fill="#1f5ee8"/><path d="M4 7l2 2 4-4" stroke="#fff" stroke-width="1.6" fill="none"/></svg>Environmental sensors</li>
  </ul>
</div>

<!-- Positioning -->
<div class="abs band pale" style="top:1229px;height:609px"></div>
<div class="abs service" style="left:168px;top:1360px">
  <h3>Positioning &amp; Monitoring</h3>
  <ul>
    <li><svg class="tick" viewBox="0 0 14 14"><circle cx="7" cy="7" r="7" fill="#1f5ee8"/><path d="M4 7l2 2 4-4" stroke="#fff" stroke-width="1.6" fill="none"/></svg>Real-Time Kinematic (RTK) Solutions</li>
    <li><svg class="tick" viewBox="0 0 14 14"><circle cx="7" cy="7" r="7" fill="#1f5ee8"/><path d="M4 7l2 2 4-4" stroke="#fff" stroke-width="1.6" fill="none"/></svg>Custom GNSS Base stations</li>
    <li><svg class="tick" viewBox="0 0 14 14"><circle cx="7" cy="7" r="7" fill="#1f5ee8"/><path d="M4 7l2 2 4-4" stroke="#fff" stroke-width="1.6" fill="none"/></svg>NTRIP service</li>
    <li><svg class="tick" viewBox="0 0 14 14"><circle cx="7" cy="7" r="7" fill="#1f5ee8"/><path d="M4 7l2 2 4-4" stroke="#fff" stroke-width="1.6" fill="none"/></svg>Tailored Monitoring Solutions</li>
    <li><svg class="tick" viewBox="0 0 14 14"><circle cx="7" cy="7" r="7" fill="#1f5ee8"/><path d="M4 7l2 2 4-4" stroke="#fff" stroke-width="1.6" fill="none"/></svg>Environmental Monitoring</li>
    <li><svg class="tick" viewBox="0 0 14 14"><circle cx="7" cy="7" r="7" fill="#1f5ee8"/><path d="M4 7l2 2 4-4" stroke="#fff" stroke-width="1.6" fill="none"/></svg>Robust communication Systems</li>
    <li><svg class="tick" viewBox="0 0 14 14"><circle cx="7" cy="7" r="7" fill="#1f5ee8"/><path d="M4 7l2 2 4-4" stroke="#fff" stroke-width="1.6" fill="none"/></svg>Internet of Things (IoT) Integration</li>
    <li><svg class="tick" viewBox="0 0 14 14"><circle cx="7" cy="7" r="7" fill="#1f5ee8"/><path d="M4 7l2 2 4-4" stroke="#fff" stroke-width="1.6" fill="none"/></svg>Solar powered systems</li>
    <li><svg class="tick" viewBox="0 0 14 14"><circle cx="7" cy="7" r="7" fill="#1f5ee8"/><path d="M4 7l2 2 4-4" stroke="#fff" stroke-width="1.6" fill="none"/></svg>Smart Sensor Networks</li>
  </ul>
</div>
<div class="abs leaf tr" style="left:617px;top:1313px;background:linear-gradient(180deg,#dbe5ee 0%,#b7c8d8 50%,#7d97b0 100%)" role="img" aria-label="White survey drone hovering against a pale sky"></div>

<!-- Design -->
<div class="abs leaf tl" style="left:141px;top:1924px;background:linear-gradient(150deg,#f0f1f2 0%,#d4d6d9 50%,#8d9196 100%)" role="img" aria-label="Machined metal parts and calipers on technical drawings"></div>
<div class="abs service" style="left:682px;top:1969px">
  <h3>Design &amp; Prototyping</h3>
  <ul>
    <li><svg class="tick" viewBox="0 0 14 14"><circle cx="7" cy="7" r="7" fill="#1f5ee8"/><path d="M4 7l2 2 4-4" stroke="#fff" stroke-width="1.6" fill="none"/></svg>Mechanical Component Design</li>
    <li><svg class="tick" viewBox="0 0 14 14"><circle cx="7" cy="7" r="7" fill="#1f5ee8"/><path d="M4 7l2 2 4-4" stroke="#fff" stroke-width="1.6" fill="none"/></svg>Robust Field Equipment Infrastructure</li>
    <li><svg class="tick" viewBox="0 0 14 14"><circle cx="7" cy="7" r="7" fill="#1f5ee8"/><path d="M4 7l2 2 4-4" stroke="#fff" stroke-width="1.6" fill="none"/></svg>Remote Monitoring System Design</li>
    <li><svg class="tick" viewBox="0 0 14 14"><circle cx="7" cy="7" r="7" fill="#1f5ee8"/><path d="M4 7l2 2 4-4" stroke="#fff" stroke-width="1.6" fill="none"/></svg>3D modelling</li>
    <li><svg class="tick" viewBox="0 0 14 14"><circle cx="7" cy="7" r="7" fill="#1f5ee8"/><path d="M4 7l2 2 4-4" stroke="#fff" stroke-width="1.6" fill="none"/></svg>Standalone Power Solutions</li>
    <li><svg class="tick" viewBox="0 0 14 14"><circle cx="7" cy="7" r="7" fill="#1f5ee8"/><path d="M4 7l2 2 4-4" stroke="#fff" stroke-width="1.6" fill="none"/></svg>Wireless Communication Solutions</li>
    <li><svg class="tick" viewBox="0 0 14 14"><circle cx="7" cy="7" r="7" fill="#1f5ee8"/><path d="M4 7l2 2 4-4" stroke="#fff" stroke-width="1.6" fill="none"/></svg>Real-Time Data Transmission</li>
    <li><svg class="tick" viewBox="0 0 14 14"><circle cx="7" cy="7" r="7" fill="#1f5ee8"/><path d="M4 7l2 2 4-4" stroke="#fff" stroke-width="1.6" fill="none"/></svg>Rapid Prototyping</li>
    <li><svg class="tick" viewBox="0 0 14 14"><circle cx="7" cy="7" r="7" fill="#1f5ee8"/><path d="M4 7l2 2 4-4" stroke="#fff" stroke-width="1.6" fill="none"/></svg>Field Deployment and Testinga</li>
  </ul>
</div>

<!-- About -->
<section class="abs about-box">
  <h2>About Us</h2>
  <p style="top:112px">Welcome to Quorvane, your reliable partner in delivering innovative solutions. Our team of skilled professionals is committed to excellence, ensuring every project is handled with precision, efficiency, &amp; integrity.</p>
  <p style="top:206px">We solve problems in the field, build robust infrastructure, and deliver accurate data to our clients. Let us help you achieve your goals with our tailored, sustainable solutions and exceptional service.</p>
  <a class="btn-dark">Read More</a>
</section>
<div class="abs about-photo" role="img" aria-label="Field team member in hi-vis on an alpine survey site with crew in the background"></div>

<!-- Case studies -->
<h2 class="abs section-title" style="top:2970px;font-weight:600;font-size:30px">Case Studies/Projects</h2>
<div class="abs arrow-btn" style="left:77px;top:3232px;background:#e7e9ee">
  <svg width="14" height="12" viewBox="0 0 14 12"><path d="M13 6H2M6 1L1 6l5 5" stroke="#111827" stroke-width="1.6" fill="none"/></svg></div>
<div class="abs arrow-btn" style="left:1089px;top:3232px;background:var(--blue-bright)">
  <svg width="14" height="12" viewBox="0 0 14 12"><path d="M1 6h11M8 1l5 5-5 5" stroke="#fff" stroke-width="1.6" fill="none"/></svg></div>

<article class="abs card" style="left:141px;top:3042px">
  <div class="ph" role="img" aria-label="Camera station with solar panel on rocky alpine ground" style="background:linear-gradient(180deg,#5d95d6 0%,#a8b1b5 55%,#6f7472 100%)"></div>
  <h4>1. Remote camera installation in Alpine Environment</h4>
  <p>Successful installation of advanced camera systems in the challenging and remote alpine regions of Fiordland.</p>
  <a class="go"><svg width="12" height="12" viewBox="0 0 12 12"><path d="M2 10L10 2M4 2h6v6" stroke="#fff" stroke-width="1.6" fill="none"/></svg></a>
</article>
<article class="abs card" style="left:618px;top:3042px">
  <div class="ph" role="img" aria-label="Survey instrument on tripod in a green paddock beside an antenna mast" style="background:linear-gradient(180deg,#c9d3dc 0%,#9cb07a 50%,#5d7a3a 100%)"></div>
  <h4>2. GNSS CORS station upgrade and survey</h4>
  <p>Upgrade and reference mark survey of GNSS Continuously Operating Reference Stations (CORS) for the NGSA positioning network.</p>
  <a class="go"><svg width="12" height="12" viewBox="0 0 12 12"><path d="M2 10L10 2M4 2h6v6" stroke="#fff" stroke-width="1.6" fill="none"/></svg></a>
</article>

<!-- Contact -->
<div class="abs contact-photo" role="img" aria-label="Technician on a ladder fitting a dish antenna to a mast above an equipment hut"></div>
<form class="abs form-panel">
  <h2>Contact Us</h2>
  <div class="field" style="left:36px;top:90px;width:208px">
    <svg width="12" height="12" viewBox="0 0 12 12"><circle cx="6" cy="4" r="2.6" fill="#b8bcc4"/><path d="M1 12c0-3 2.2-4.6 5-4.6S11 9 11 12Z" fill="#b8bcc4"/></svg>First Name</div>
  <div class="field" style="left:284px;top:90px;width:208px">
    <svg width="12" height="12" viewBox="0 0 12 12"><circle cx="6" cy="4" r="2.6" fill="#b8bcc4"/><path d="M1 12c0-3 2.2-4.6 5-4.6S11 9 11 12Z" fill="#b8bcc4"/></svg>Last Name</div>
  <div class="field" style="left:36px;top:138px;width:208px">
    <svg width="12" height="10" viewBox="0 0 12 10"><rect x="0.5" y="0.5" width="11" height="9" rx="1" fill="none" stroke="#b8bcc4"/><path d="M1 1l5 4 5-4" stroke="#b8bcc4" fill="none"/></svg>Email Address</div>
  <div class="field" style="left:284px;top:138px;width:208px">
    <svg width="12" height="12" viewBox="0 0 12 12"><path d="M2 1l2 0 1 3-1.5 1a7 7 0 0 0 3.5 3.5L8 7l3 1v2c0 .6-.4 1-1 1A9 9 0 0 1 1 2c0-.6.4-1 1-1Z" fill="none" stroke="#b8bcc4"/></svg>Phone Number</div>
  <div class="field" style="left:36px;top:188px;width:456px;height:36px">
    <svg width="12" height="12" viewBox="0 0 12 12"><rect x="0.5" y="0.5" width="11" height="11" rx="1" fill="none" stroke="#b8bcc4"/><path d="M3 9l1-3 4-4 2 2-4 4Z" fill="#b8bcc4"/></svg>Message</div>
  <a class="btn-submit">Submit</a>
</form>
<div class="abs board-photo" role="img" aria-label="Open enclosure with wired power regulator and data logger"></div>
<div class="abs years"><b>15+</b><span>Years Experience</span></div>

<!-- Newsletter -->
<svg class="abs" style="left:440px;top:4330px" width="300" height="140" viewBox="0 0 300 140" aria-hidden="true">
  <path d="M10 30L290 10 170 130 130 80Z" fill="#e9eef8" opacity=".7"/>
</svg>
<h2 class="abs news-title">Subscribe To Our Newsletter</h2>
<p class="abs news-note">By subscribing, you agree with our privacy policy and our terms of service.</p>
<div class="abs news-form">Enter Email Address<a class="sub">Subscribe</a></div>

<!-- Footer -->
<svg class="abs footer-wave" width="1200" height="130" viewBox="0 0 1200 130" aria-hidden="true">
  <path d="M0 60C150 10 330 10 520 55S900 110 1200 20V130H0Z" fill="#2f6be8"/>
  <path d="M0 80C160 35 340 40 520 80S900 130 1200 50V130H0Z" fill="#070c3a"/>
</svg>
<footer class="abs footer">
  <div class="brand" style="position:absolute;left:141px;top:100px;font-size:30px"><span class="dot"></span>Quorvane</div>
  <p class="about">We are field operations experts with backgrounds in surveying, geoscience, and technical field work. Our purpose is to solve problems in the field, build robust infrastructure and deliver accurate data to clients.</p>
  <h5 style="left:467px;top:75px">Quick <b>Links</b></h5>
  <ul class="links"><li>Home</li><li>What We Do</li><li>About</li><li>Projects</li><li>Contact</li></ul>
  <h5 style="left:614px;top:75px">Contact <b>Details</b></h5>
  <div class="cd" style="top:105px">
    <svg width="12" height="14" viewBox="0 0 12 14"><path d="M6 0a5 5 0 0 1 5 5c0 4-5 9-5 9S1 9 1 5a5 5 0 0 1 5-5Z" fill="#fff"/><circle cx="6" cy="5" r="2" fill="#070c3a"/></svg>
    <span>123, Building Name, Street<br>City, State XY 123456</span></div>
  <div class="cd" style="top:165px">
    <svg width="12" height="12" viewBox="0 0 12 12"><path d="M2 1h2l1 3-1.5 1a7 7 0 0 0 3.5 3.5L8 7l3 1v2c0 .6-.4 1-1 1A9 9 0 0 1 1 2c0-.6.4-1 1-1Z" fill="#fff"/></svg>
    <span><b>Phone</b>123 456 7890</span></div>
  <div class="cd" style="top:225px">
    <svg width="12" height="10" viewBox="0 0 12 10"><rect width="12" height="10" rx="1" fill="#fff"/><path d="M1 1l5 4 5-4" stroke="#070c3a" fill="none"/></svg>
    <span><b>Email</b>hi@quorvane.nz</span></div>
  <div class="big-mark" aria-hidden="true"></div>
  <p class="copy">© 2024 Quorvane. All Rights Reserved.</p>
  <p class="legal">Privacy Policy | Disclaimer</p>
</footer>

</body>
</html>
```